Tide Works - Logo & Business Card

I have briefly designed a logo for my small events business and need it fixed up. I would prefer it to be white on black background. I also need a PDF for business cards, I would like them to be black with the logo on one side and my details on the other side:

Tide Works
Corinne-Mae Talbisk
Founder / Director
0492 817 403
corinne@tideworks.com.au

Industry/Entity Type

Events

```html
<!DOCTYPE html>
<html lang="en">
<head>
<meta charset="utf-8">
<title>Tide Works – Business Card</title>
<link rel="stylesheet" href="https://fonts.googleapis.com/css2?family=Arimo:wght@400;700&display=swap">
<style>
  :root {
    --backdrop: #e9e7e3;
    --card: #111111;
    --ink: #ffffff;
    --icon-cut: #111111;
    --wave-fill: #7bcfd3;
    --wave-edge: #12b48e;
    --brand: #5fcfcc;
  }
  * { box-sizing: border-box; margin: 0; padding: 0; }
  html, body {
    width: 1200px; height: 870px; overflow: hidden;
    background: var(--backdrop);
    font-family: "Arimo", Arial, sans-serif;
  }
  .sheet {
    width: 1200px; height: 870px;
    display: flex; justify-content: center; align-items: center; gap: 80px;
  }
  .card {
    position: relative;
    width: 440px; height: 700px;
    background: var(--card);
    box-shadow: 0 6px 18px rgba(0,0,0,0.25);
    overflow: hidden;
  }
  .card__wave { position: absolute; inset: 0; width: 100%; height: 100%; }
  .holder { position: absolute; left: 60px; top: 92px; color: var(--ink); }
  .holder__name { font-size: 25px; font-weight: 400; letter-spacing: 0.2px; white-space: nowrap; }
  .holder__role { font-size: 17px; margin-top: 6px; }
  .brand {
    position: absolute; left: 0; right: 0;
    display: flex; align-items: center; justify-content: center; gap: 14px;
    color: var(--brand); font-weight: 400; white-space: nowrap;
  }
  .brand__dot { width: 18px; height: 18px; border-radius: 50%; background: var(--brand); }
  .card--front .brand { top: 262px; font-size: 38px; }
  .card--back .brand { top: 250px; font-size: 48px; }
  .contact {
    position: absolute; left: 60px; top: 420px;
    list-style: none; color: var(--ink); font-size: 21px;
  }
  .contact__item { display: flex; align-items: center; gap: 18px; margin-bottom: 12px; white-space: nowrap; }
  .contact__icon { width: 22px; height: 18px; flex: none; }
</style>
</head>
<body>
<main class="sheet">
  <article class="card card--front">
    <svg class="card__wave" viewBox="0 0 440 700" preserveAspectRatio="none" aria-hidden="true">
      <path d="M0 655 C40 622 90 640 150 640 C230 640 300 565 350 535 C390 510 420 512 440 522 L440 700 L0 700 Z" fill="var(--wave-fill)"/>
      <path d="M0 655 C40 622 90 640 150 640 C230 640 300 565 350 535 C390 510 420 512 440 522" fill="none" stroke="var(--wave-edge)" stroke-width="9"/>
    </svg>
    <div class="holder">
      <p class="holder__name">Corinne-Mae Talbisk</p>
      <p class="holder__role">Founder / Director</p>
    </div>
    <div class="brand"><span class="brand__dot"></span><span class="brand__name">Tide Works</span></div>
    <ul class="contact">
      <li class="contact__item">
        <svg class="contact__icon" viewBox="0 0 22 18" aria-hidden="true">
          <path d="M2 6 C2 2 20 2 20 6 L16 7 L15 5 H7 L6 7 Z" fill="#ffffff"/>
          <rect x="4" y="9" width="14" height="8" rx="2" fill="#ffffff"/>
          <circle cx="11" cy="13" r="2" fill="var(--icon-cut)"/>
        </svg>
        <span>0492 817 403</span>
      </li>
      <li class="contact__item">
        <svg class="contact__icon" viewBox="0 0 22 18" aria-hidden="true">
          <rect x="1" y="3" width="20" height="13" fill="#ffffff"/>
          <path d="M1 3 L11 11 L21 3" fill="none" stroke="var(--icon-cut)" stroke-width="1.5"/>
        </svg>
        <span>corinne@tideworks.com.au</span>
      </li>
    </ul>
  </article>

  <article class="card card--back">
    <svg class="card__wave" viewBox="0 0 440 700" preserveAspectRatio="none" aria-hidden="true">
      <path d="M0 610 C70 630 120 600 190 570 C270 535 330 520 380 525 C410 528 430 540 440 550 L440 700 L0 700 Z" fill="var(--wave-fill)"/>
      <path d="M0 610 C70 630 120 600 190 570 C270 535 330 520 380 525 C410 528 430 540 440 550" fill="none" stroke="var(--wave-edge)" stroke-width="9"/>
    </svg>
    <div class="brand"><span class="brand__dot"></span><span class="brand__name">Tide Works</span></div>
  </article>
</main>
</body>
</html>
```